Animal Hospital Business Cards

Make a business card look like the attached example

*Use the same blue/black coloring
*Fenbrook Hollow Animal Hospital (instead of mobile pet rounds)
*Emergency Services (instead of tri-county care center)
*House Calls (instead of open 7 days by appointment)
*Change address to 1873 Tilden Marsh Rd Loveland, OH 45140
*Open 7 days a week (instead of emergency service)
*Add the website www.fenbrookhollowanimalhospital.example

On the back...
*instead of the text outlined in red, just white
*instead of the light blue, try your best to make it just like the blue and black on the front side of the card
*Delete "designed and printed by Blue Heron Print Co, www.blueheronprintco.example

Requirements
Must have
• look just like the attached example with requested edits/changes

```html
<!DOCTYPE html>
<html lang="en">
<head>
<meta charset="utf-8">
<title>Fenbrook Hollow Animal Hospital – Business Card</title>
<link href="https://fonts.googleapis.com/css2?family=Ubuntu:wght@500;700&family=Tinos:wght@400;700&family=Roboto+Condensed:wght@400;500&family=Lato:wght@400;700&family=Open+Sans:wght@400&display=swap" rel="stylesheet">
<style>
  :root {
    --teal: #2b7893;
    --ink: #1a1a1a;
    --grey-text: #555555;
    --paper: #ffffff;
    --backdrop: #6d6d6d;
  }
  * { margin: 0; padding: 0; box-sizing: border-box; }
  html, body { width: 1200px; height: 802px; overflow: hidden; background: var(--backdrop); }
  .stage { position: relative; width: 1200px; height: 802px; }

  .card {
    position: absolute; top: 274px; width: 442px; height: 265px;
    background: var(--paper);
    box-shadow: 2px 3px 6px rgba(0,0,0,.35);
    overflow: hidden;
  }
  .card-front { left: 136px; }
  .card-back { left: 624px; }
  .band {
    position: absolute; left: 0; width: 100%;
    background: var(--teal); color: var(--paper);
    display: flex; align-items: center; justify-content: center; flex-direction: column;
  }
  .abs { position: absolute; }

  /* Front */
  .front-header { top: 0; height: 50px; font: 700 20px 'Ubuntu', sans-serif; letter-spacing: .2px; }
  .front-footer { bottom: 0; height: 43px; font: 700 18px 'Ubuntu', sans-serif; letter-spacing: .4px; }
  .doctor-name { left: 0; width: 100%; top: 64px; text-align: center; font: 700 17px 'Tinos', serif; color: var(--ink); }
  .website { left: 0; width: 100%; top: 88px; text-align: center; font: 400 12px 'Roboto Condensed', sans-serif; color: var(--ink); }
  .emergency { left: 20px; top: 134px; font: 400 14px/17px 'Open Sans', sans-serif; color: var(--ink); }
  .species { left: 126px; top: 138px; font: 400 12.5px 'Open Sans', sans-serif; color: var(--ink); word-spacing: 1px; }
  .species .dot { font-size: 10px; margin: 0 3px; }
  .house-calls { right: 24px; top: 137px; font: 400 14px 'Open Sans', sans-serif; color: var(--ink); }
  .address { left: 20px; top: 174px; font: 400 10px/14px 'Roboto Condensed', sans-serif; color: var(--ink); }
  .phone { left: 150px; top: 176px; font: 500 22px 'Roboto Condensed', sans-serif; color: var(--teal); }
  .experience { right: 27px; top: 174px; text-align: center; font: 400 10px/14px 'Roboto Condensed', sans-serif; color: var(--ink); }

  /* Back */
  .back-header { top: 0; height: 59px; font: 400 19px 'Lato', sans-serif; letter-spacing: .2px; }
  .back-footer { bottom: 0; height: 62px; }
  .back-footer .sign-name { font: 400 15px 'Tinos', serif; line-height: 18px; }
  .back-footer .sign-phone { font: 400 14px 'Lato', sans-serif; line-height: 17px; }
  .form-line { left: 36px; right: 36px; font: 400 14px 'Lato', sans-serif; color: var(--grey-text); display: flex; align-items: baseline; white-space: nowrap; }
  .fill { border-bottom: 1.5px dotted var(--grey-text); margin: 0 2px; height: 1px; }
  .line-for { top: 85px; }
  .line-date { top: 130px; left: 36px; }
  .days { top: 169px; left: 37px; right: 36px; display: flex; justify-content: space-between; font: 400 13px 'Lato', sans-serif; color: var(--grey-text); }
  .day { display: flex; align-items: center; gap: 3px; }
  .box { width: 15px; height: 15px; border: 1.3px solid var(--grey-text); display: inline-block; }
</style>
</head>
<body>
<div class="stage">

  <section class="card card-front">
    <div class="band front-header">Fenbrook Hollow Animal Hospital</div>
    <div class="abs doctor-name">Gregory L. Halvorsen, DVM</div>
    <div class="abs website">www.fenbrookhollowanimalhospital.example</div>
    <div class="abs emergency">Emergency<br>Services</div>
    <div class="abs species">Cats<span class="dot">●</span>Dogs <span class="dot">●</span> Birds<span class="dot">●</span>Exotics</div>
    <div class="abs house-calls">House Calls</div>
    <div class="abs address">1873 Tilden Marsh Rd<br>Loveland, OH 45140</div>
    <div class="abs phone">(513) 555-0147</div>
    <div class="abs experience">38 years of<br>experience</div>
    <div class="band front-footer">OPEN 7 DAYS A WEEK</div>
  </section>

  <section class="card card-back">
    <div class="band back-header">VETERINARY APPOINTMENT</div>
    <div class="abs form-line line-for">YOUR APPOINTMENT FOR <span class="fill" style="width:136px"></span>IS ON</div>
    <div class="abs form-line line-date">Date :&nbsp;<span class="fill" style="width:108px"></span>&nbsp;&nbsp;&nbsp;&nbsp;Time :&nbsp;<span class="fill" style="width:98px"></span>&nbsp;AM / PM</div>
    <div class="abs days">
      <span class="day"><span class="box"></span>MON</span>
      <span class="day"><span class="box"></span>TUE</span>
      <span class="day"><span class="box"></span>WED</span>
      <span class="day"><span class="box"></span>THU</span>
      <span class="day"><span class="box"></span>FRI</span>
      <span class="day"><span class="box"></span>SAT</span>
    </div>
    <div class="band back-footer">
      <span class="sign-name">Gregory L. Halvorsen, DVM</span>
      <span class="sign-phone">513.555.0147</span>
    </div>
  </section>

</div>
</body>
</html>
```